Tallgrove Financial Business Card Design

We are looking for a nice looking business card design. I'd prefer something other than white for the background but white is ok if necessary. I'm uploading two versions of my picture, one is square and one is rounded. Also a couple of versions of the logo for white backgrounds as well as one for darker backgrounds.

Target Market(s)

Realtors and prospective clients

Industry/Entity Type

Mortgage

Contact Information for Business Card

Double sided business card. Not sure what is needed here.

Colors

Designer to choose colors to be used in the design.

Requirements
Must have
• Name: Marcus Ellery
• Title: Senior Mortgage Advisor
• Email: marcusellery@tallgrovefinancial-mail.net
• website: www.marcusellerymortgagecrew-site.com
• Address: 4725 W 860 N, STE 310 Salt Lake City, UT 84199
• Phone: 801-555-0187
• nmls# 482917
• Logo is on our webstie. www.tallgrovefinancial-mail.net
• Picture
Nice to have
• Colors could be similar to our website www.tallgrovefinancial-mail.net
• A list of what we do (VA Loans, FHA Loans, Conventional Loans, USDA Loans)

```html
<!DOCTYPE html>
<html lang="en">
<head>
<meta charset="utf-8">
<title>Tallgrove Financial Business Card</title>
<link href="https://fonts.googleapis.com/css2?family=Cinzel:wght@700&family=Questrial&display=swap" rel="stylesheet">
<style>
  :root {
    --stage: #2a2a2a;
    --card: #262626;
    --card-edge: #1c1c1c;
    --silver: #d4d4d4;
    --text: #e6e6e6;
    --muted: #b5b5b5;
    --rule: #9a9a9a;
  }
  html, body {
    margin: 0;
    padding: 0;
    width: 1200px;
    height: 834px;
    overflow: hidden;
    background: var(--stage);
  }
  .canvas {
    position: relative;
    width: 1200px;
    height: 834px;
    background: var(--stage);
  }
  .card {
    position: absolute;
    width: 560px;
    height: 320px;
    background: var(--card);
    border: 1px solid var(--card-edge);
    box-shadow: 0 12px 30px rgba(0,0,0,0.45);
    font-family: "Questrial", sans-serif;
    color: var(--text);
  }
  .card-front { left: 90px; top: 90px; }
  .card-back { left: 550px; top: 420px; }

  .brand {
    position: absolute;
    left: 0;
    right: 0;
    display: flex;
    align-items: center;
    justify-content: center;
    gap: 12px;
  }
  .card-front .brand { top: 136px; }
  .card-back .brand { top: 70px; }
  .brand-mark {
    width: 14px;
    height: 14px;
    border-radius: 50%;
    background: var(--silver);
  }
  .brand-name {
    font-family: "Cinzel", serif;
    font-weight: 700;
    font-size: 28px;
    letter-spacing: 2px;
    color: var(--silver);
  }

  .person {
    position: absolute;
    left: 60px;
    top: 190px;
    font-size: 13px;
    line-height: 1.5;
    color: var(--muted);
  }
  .person-name {
    font-size: 16px;
    font-weight: 700;
    color: var(--text);
    margin-bottom: 2px;
  }
  .divider {
    position: absolute;
    left: 300px;
    top: 160px;
    width: 1px;
    height: 90px;
    background: var(--rule);
  }
  .contact {
    position: absolute;
    left: 318px;
    top: 160px;
    font-size: 12px;
    line-height: 1.65;
    color: var(--muted);
  }
</style>
</head>
<body>
  <main class="canvas">
    <section class="card card-front" aria-label="Card front">
      <div class="brand">
        <span class="brand-mark"></span>
        <span class="brand-name">Tallgrove Financial</span>
      </div>
    </section>

    <section class="card card-back" aria-label="Card back">
      <div class="brand">
        <span class="brand-mark"></span>
        <span class="brand-name">Tallgrove Financial</span>
      </div>

      <div class="person">
        <div class="person-name">Marcus Ellery</div>
        <div>Senior Mortgage Advisor</div>
        <div>4725 W 860 N, STE 310 Salt</div>
        <div>Lake City, UT 84199</div>
      </div>

      <div class="divider"></div>

      <div class="contact">
        <div>801-555-0187</div>
        <div>marcusellery@tallgrovefinancial-mail.net</div>
        <div>www.marcusellerymortgagecrew-site.com</div>
        <div>nmls : 482917</div>
      </div>
    </section>
  </main>
</body>
</html>
```